I want your CD Cover design for my next singe "After Marlow Fell"

I'm looking for a CD cover based on my song "After Marlow Fell". It's a reflection on the passing of my musical influences (Conrad Vessel, Tam Quill, Gilbert Ashmore) and other (e.g. Jubal), and on those still with us (e.g. Pettigrew) and what we do when those who influenced us most are gone from our lives.

You should be able to listen to a private demo unreleased version here:

https://www.tunevault-example.com/lowfenguild/song/58302417-after-marlow-fell-demo-mix-rn

I prefer influenced/metaphoric images vs. direct copies (e.g. no pictures of famous musicians), but I'll leave that to your creativity for the details.

Looking forward to seeing everyone's designs!

Oskar Tremaine
c/o Low Fen Guild
www.lowfenguild-example.com

Target Market(s)

Indie-pop, classic rock

Requirements
Must have
• Low Fen Guild logo in the image (eps and psd files provided)
• After Marlow Fell logo in the image
Should not have
• Should not have direct pictures of musicians noted above on the artwork
• Should not have my name (Oskar Tremaine) on the artwork
• Should not have the website on the artwork

```html
<!DOCTYPE html>
<html lang="en">
<head>
<meta charset="utf-8">
<title>Low Fen Guild – After Marlow Fell</title>
<link rel="stylesheet" href="https://fonts.googleapis.com/css2?family=Advent+Pro:wght@200;300;400&display=swap">
<style>
  :root {
    --backdrop: #e4e4e6;
    --sky-deep: #2a1f8f;
    --sky-blue: #1d55b8;
    --sky-teal: #2a9fbf;
    --cloud-aqua: rgba(120, 210, 220, 0.45);
    --horizon-gold: #c9a866;
    --sea-blue: #1c7fd0;
    --pier-grey: #77716b;
    --pier-dark: #3b3836;
    --band-white: #ffffff;
    --title-ink: #1b1a1c;
  }
  * { margin: 0; padding: 0; box-sizing: border-box; }
  html, body {
    width: 1200px;
    height: 792px;
    overflow: hidden;
    background: var(--backdrop);
  }
  .canvas {
    position: relative;
    width: 1200px;
    height: 792px;
  }
  .cover {
    position: absolute;
    left: 290px;
    top: 86px;
    width: 620px;
    height: 620px;
    overflow: hidden;
    box-shadow: 0 10px 30px rgba(0,0,0,0.18);
  }
  .cover-photo {
    position: absolute;
    inset: 0;
    background:
      radial-gradient(ellipse 55% 22% at 30% 38%, var(--cloud-aqua), transparent 70%),
      radial-gradient(ellipse 40% 18% at 78% 30%, rgba(90, 170, 230, 0.35), transparent 70%),
      radial-gradient(ellipse 60% 12% at 55% 55%, rgba(230, 190, 110, 0.45), transparent 75%),
      linear-gradient(
        to bottom,
        var(--sky-deep) 0%,
        var(--sky-blue) 20%,
        var(--sky-teal) 38%,
        var(--horizon-gold) 54%,
        var(--sea-blue) 61%,
        var(--sea-blue) 67%,
        var(--pier-grey) 73%,
        var(--pier-dark) 100%
      );
  }
  .band-name {
    position: absolute;
    left: 215px;
    top: 58px;
    font-family: "Advent Pro", sans-serif;
    font-weight: 300;
    color: var(--band-white);
    text-transform: uppercase;
    line-height: 0.95;
    letter-spacing: 4px;
  }
  .band-name span { display: block; font-size: 74px; }
  .band-name .line-2 { padding-left: 40px; }
  .band-name .line-3 { padding-left: 80px; font-size: 64px; }
  .release-title {
    position: absolute;
    left: 44px;
    right: 30px;
    bottom: 30px;
    font-family: "Advent Pro", sans-serif;
    font-weight: 400;
    font-size: 46px;
    letter-spacing: 5px;
    text-transform: uppercase;
    color: var(--title-ink);
    white-space: nowrap;
  }
</style>
</head>
<body>
  <main class="canvas">
    <section class="cover">
      <div class="cover-photo" role="img" aria-label="Photograph: a woman seen from behind walking along a seaside pier among a flock of gulls, under a blue and golden sky with soft bokeh light dots"></div>
      <h1 class="band-name">
        <span class="line-1">Low</span>
        <span class="line-2">Fen</span>
        <span class="line-3">Guild</span>
      </h1>
      <h2 class="release-title">After Marlow Fell...</h2>
    </section>
  </main>
</body>
</html>
```